Creative Landscape Architecture Company Needs a Creative Business Card Design

Marsh and Partners, Inc. is a landscape architecture (LA) company started in 1997 in Austin, TX. We work on large commerical projects all around the U.S. and provide land planning, site planning, landscape design and architectural renderings.

We don't want this card to look like a LA firm's business card. We are looking for a business card design that is edgy and cool to reflect the more artistic and creative side of our company. We would like our clients to think "now there's a business card unlike any other LA that I've seen before."

We would like it to be in standard 2"x3.5" format. Double sided. Full color ok. Our company logo is attached. We like the logo but would not be adverse to any variations you would like to make to it. Feel free to change it up. Typically the logo has been a light saturated orange color but its not necessary that you stick with it.

Requirements
Must have
• 1. Company name
2. individuals name
3. email address
4. cell number
5. office number
6. website: www.marshandpartners-demo.net
7. Business address
Nice to have
• Can add (but not necessary)
Personal titles such as "president" or "registered landscape architect"

```html
<!DOCTYPE html>
<html lang="en">
<head>
<meta charset="utf-8">
<title>Marsh and Partners, Inc. – Business Card</title>
<link rel="stylesheet" href="https://fonts.googleapis.com/css2?family=PT+Sans:wght@400;700&family=Marcellus&display=swap">
<style>
  :root {
    --page-bg: #e9e5df;
    --card-white: #ffffff;
    --card-grey: #5b5b5d;
    --ink-black: #111111;
    --ink-white: #ffffff;
    --ink-soft: #e4e4e4;
    --logo-block: #141414;
  }
  * { margin: 0; padding: 0; box-sizing: border-box; }
  html, body {
    width: 1200px; height: 402px; overflow: hidden;
    background: var(--page-bg);
    font-family: "PT Sans", Arial, sans-serif;
  }
  .stage { position: relative; width: 1200px; height: 402px; }
  .card {
    position: absolute; top: 66px;
    width: 559px; height: 298px;
    transform: scale(0.975); transform-origin: top left;
    overflow: hidden;
    box-shadow: 0 2px 6px rgba(0,0,0,0.25);
  }
  .card--front { left: 61px; background: var(--card-white); }
  .card--back { left: 630px; background: var(--card-grey); }

  .front-wave { position: absolute; inset: 0; }

  .logo-mark {
    position: absolute; left: 83px; top: 52px;
    width: 96px; height: 160px;
    background: var(--logo-block);
  }
  .company-name {
    position: absolute; left: 0; width: 270px; top: 220px;
    text-align: center;
    font-family: "Marcellus", Georgia, serif;
    font-size: 21px; color: var(--ink-black);
    white-space: nowrap;
  }

  .contact {
    position: absolute; right: 67px; top: 56px;
    text-align: right; color: var(--ink-white);
  }
  .contact__name { font-size: 17px; font-weight: 700; line-height: 20px; }
  .contact__title { font-size: 10px; color: var(--ink-soft); line-height: 14px; }
  .contact__address { margin-top: 16px; font-size: 13px; line-height: 15px; }
  .contact__lines { margin-top: 20px; font-size: 13px; line-height: 18.5px; }
  .contact__line { position: relative; white-space: nowrap; }
  .contact__icon {
    position: absolute; right: -17px; top: 4px;
    width: 11px; height: 11px; fill: var(--ink-white);
  }

  .back-name {
    position: absolute; left: 0; right: 0; top: 126px;
    display: flex; justify-content: center; align-items: center; gap: 10px;
    font-family: "Marcellus", Georgia, serif;
    font-size: 24px; color: var(--ink-black);
  }
  .back-name__square { width: 16px; height: 16px; background: var(--logo-block); }
  .back-web {
    position: absolute; left: 0; right: 0; top: 266px;
    text-align: center;
    font-size: 16px; letter-spacing: 1.5px; color: var(--ink-black);
  }
</style>
</head>
<body>
<main class="stage">

  <section class="card card--front" aria-label="Business card front">
    <svg class="front-wave" viewBox="0 0 559 298" aria-hidden="true">
      <path d="M290 0 C 270 70, 262 140, 268 200 C 272 245, 285 275, 300 298 L559 298 L559 0 Z" fill="var(--card-grey)"/>
      <path d="M283 0 C 262 70, 254 140, 260 200 C 264 245, 277 275, 292 298" fill="none" stroke="var(--ink-black)" stroke-width="5"/>
      <path d="M276 0 C 255 70, 247 140, 253 200 C 257 245, 270 275, 285 298" fill="none" stroke="var(--ink-black)" stroke-width="1.2"/>
    </svg>

    <div class="logo-mark" aria-hidden="true"></div>
    <div class="company-name">Marsh and Partners, Inc.</div>

    <div class="contact">
      <div class="contact__name">Your name</div>
      <div class="contact__title">Registered Landscape Architect</div>
      <div class="contact__address">Street Name<br>City Name<br>State Zip Code</div>
      <div class="contact__lines">
        <div class="contact__line">555-014-2290
          <svg class="contact__icon" viewBox="0 0 12 12" aria-hidden="true"><path d="M2.5 1 L4.5 1 L5.5 3.8 L4.2 4.8 C4.9 6.3 5.8 7.2 7.2 7.8 L8.2 6.5 L11 7.5 L11 9.5 C11 10.4 10.3 11 9.5 11 C5 10.7 1.3 7 1 2.5 C1 1.7 1.6 1 2.5 1 Z"/></svg>
        </div>
        <div class="contact__line">555-014-2290
          <svg class="contact__icon" viewBox="0 0 12 12" aria-hidden="true"><path d="M3.5 0.5 H8.5 A1 1 0 0 1 9.5 1.5 V10.5 A1 1 0 0 1 8.5 11.5 H3.5 A1 1 0 0 1 2.5 10.5 V1.5 A1 1 0 0 1 3.5 0.5 Z M3.8 2 V8.5 H8.2 V2 Z M6 9.3 A0.8 0.8 0 1 0 6 10.9 A0.8 0.8 0 1 0 6 9.3 Z"/></svg>
        </div>
        <div class="contact__line">marshpartners@demo-mail.com
          <svg class="contact__icon" viewBox="0 0 12 12" aria-hidden="true"><path d="M1 3 H11 V10 H1 Z M1.6 3.4 L6 7 L10.4 3.4" stroke="var(--card-grey)" stroke-width="0.9"/></svg>
        </div>
        <div class="contact__line">www.marshandpartners-demo.net
          <svg class="contact__icon" viewBox="0 0 12 12" aria-hidden="true"><circle cx="6" cy="6" r="5"/><path d="M1 6 H11 M6 1 V11 M6 1 C3.5 3.5 3.5 8.5 6 11 M6 1 C8.5 3.5 8.5 8.5 6 11" fill="none" stroke="var(--card-grey)" stroke-width="0.8"/></svg>
        </div>
      </div>
    </div>
  </section>

  <section class="card card--back" aria-label="Business card back">
    <div class="back-name">
      <span class="back-name__square" aria-hidden="true"></span>
      <span>Marsh and Partners, Inc.</span>
    </div>
    <div class="back-web">www.marshandpartners-demo.net</div>
  </section>

</main>
</body>
</html>
```